Poster design for the WILLOW WISP magic show.

We need a poster design for our magic show. This isn't your typical 'small town' magic show. Our show features world class magicians from the Velvet Lantern, in Hollywood California. The show is geared toward everyone, it is family friendly - with a little bit of an edge. We want people to see the poster and feel like they are going to have a unique and sophisticated magical experience. We also want individuals and couples to see the poster and feel like it is a show for them and not only for children.
Updates

Target Market(s)

BRT audience, family audience, the age range is anywhere from 5 - 105. Cool people.

Industry/Entity Type

Town

Requirements
Must have
• Our attached .jpg of the magician floating in the air. Poster size 24x36"
Must have text:
The 3rd Annual Albuquerque Conjuring Gala Presents (small type)
Willow Wisp (should be larger type)
November 24th - 25th
Showtimes 3:00PM & 7:30PM Saturday, 2:00PM Sunday
Tickets available at www.DorvaSeats.example For more information contact Dorva Theatre @ 505.555.0147
Nice to have
• A sort of old school/antique feeling to the poster.
Perhaps a theater marquee
Check out www.grovelumen.example - we love the feeling of this site for our poster...
Feel free to adjust the provided .jpg accordingly in regards to color/size/interaction with the rest of the poster
Should not have
• Should not have clowns, bunnies, anything that would make it feel like a 3 year old's magic themed birthday party.

```html
<!DOCTYPE html>
<html lang="en">
<head>
<meta charset="utf-8">
<title>Willow Wisp – Albuquerque Conjuring Gala</title>
<link href="https://fonts.googleapis.com/css2?family=Russo+One&family=Cabin:ital,wght@0,500;0,700;1,500;1,700&family=Ubuntu:wght@700&display=swap" rel="stylesheet">
<style>
  :root {
    --night: #120806;
    --ember: #7a2608;
    --flame: #e0620f;
    --glow: #ffb347;
    --title-fill: #3a1708;
    --gold: #ffe81f;
    --band: #7c0d06;
    --band-edge: #f07a12;
    --link: #5a8cff;
    --white: #ffffff;
  }
  html, body { margin: 0; padding: 0; overflow: hidden; background: var(--night); }
  .poster {
    position: relative;
    width: 800px; height: 1200px;
    overflow: hidden;
    background:
      radial-gradient(ellipse 430px 620px at 400px 560px, var(--glow) 0%, var(--flame) 35%, var(--ember) 70%, var(--night) 100%);
    font-family: "Cabin", sans-serif;
    color: var(--white);
  }
  .ornament {
    position: absolute; top: 0; width: 150px; height: 190px;
    background: radial-gradient(circle at 50% 45%, #b5653a 0%, #5a2c16 60%, rgba(40,20,10,0) 100%);
  }
  .ornament--left { left: 0; }
  .ornament--right { right: 0; }
  .stage-lights { position: absolute; top: 8px; left: 180px; width: 380px; height: 24px; }
  .stage-photo {
    position: absolute; left: 95px; top: 580px; width: 680px; height: 380px;
    background: radial-gradient(ellipse at 45% 55%, #b2571e 0%, #8a3810 55%, rgba(122,38,8,0) 100%);
  }
  .headline { position: absolute; inset: 0; width: 800px; height: 600px; }
  .info-band { position: absolute; left: 0; top: 960px; width: 800px; height: 240px; }
  .info {
    position: absolute; left: 0; top: 1022px; width: 800px;
    text-align: center;
  }
  .info p { margin: 0; }
  .dates { font-weight: 700; font-size: 33px; color: var(--gold); line-height: 40px; letter-spacing: .5px; }
  .times { font-size: 20px; font-weight: 500; margin-top: 16px !important; }
  .times b { font-weight: 700; }
  .tickets, .contact { font-style: italic; font-size: 20px; font-weight: 500; margin-top: 12px !important; }
  .tickets a { color: var(--link); font-weight: 700; text-decoration: none; }
  .contact b { font-weight: 700; }
</style>
</head>
<body>
<div class="poster">
  <div class="ornament ornament--left" role="img" aria-label="Ornate bronze winged dragon ornament"></div>
  <div class="ornament ornament--right" role="img" aria-label="Ornate bronze winged dragon ornament"></div>

  <svg class="stage-lights" viewBox="0 0 380 24" aria-hidden="true">
    <circle cx="20" cy="12" r="10" fill="#ff4b3a"/>
    <circle cx="65" cy="12" r="10" fill="#ffd23a"/>
    <circle cx="110" cy="12" r="10" fill="#ff5a7a"/>
    <circle cx="305" cy="12" r="10" fill="#ffb030"/>
    <circle cx="350" cy="12" r="10" fill="#ff7a2a"/>
  </svg>

  <div class="stage-photo" role="img" aria-label="Magician levitating in mid-air on stage, holding a yellow chair, beside a small table"></div>

  <svg class="headline" viewBox="0 0 800 600">
    <defs>
      <path id="subtitle-arc" d="M 22 240 Q 380 150 780 180"/>
      <filter id="title-glow" x="-10%" y="-20%" width="120%" height="140%">
        <feGaussianBlur stdDeviation="8" result="b"/>
        <feFlood flood-color="#ffb030" flood-opacity=".8"/>
        <feComposite in2="b" operator="in"/>
        <feMerge><feMergeNode/><feMergeNode in="SourceGraphic"/></feMerge>
      </filter>
    </defs>

    <g class="edition" font-family="Ubuntu, sans-serif" font-weight="700" stroke="#1a0a04" stroke-width="6" paint-order="stroke" stroke-linejoin="round">
      <text x="178" y="72" font-size="40" fill="#ffffff" transform="rotate(-6 215 60)">THE</text>
      <text x="280" y="118" font-size="118" fill="#ffe81f">3</text>
      <text x="350" y="52" font-size="44" fill="#ffe81f" transform="rotate(-6 380 40)">rd</text>
    </g>

    <text font-family="Cabin, sans-serif" font-weight="500" font-size="34" fill="#ffffff" stroke="#2a0f05" stroke-width="5" paint-order="stroke" stroke-linejoin="round">
      <textPath href="#subtitle-arc" textLength="750" lengthAdjust="spacingAndGlyphs">Annual Albuquerque Conjuring Gala Presents</textPath>
    </text>

    <g class="title" font-family="'Russo One', sans-serif" fill="var(--title-fill)" stroke="#ffffff" stroke-width="4" paint-order="stroke" filter="url(#title-glow)">
      <text x="38" y="372" font-size="150" textLength="730" lengthAdjust="spacingAndGlyphs" stroke-linejoin="round">WILLOW</text>
      <text x="48" y="548" font-size="150" textLength="712" lengthAdjust="spacingAndGlyphs" stroke-linejoin="round">WISP</text>
    </g>
  </svg>

  <svg class="info-band" viewBox="0 0 800 240" aria-hidden="true">
    <path d="M0 70 Q 360 -10 800 40 L800 240 L0 240 Z" fill="var(--band-edge)"/>
    <path d="M0 82 Q 360 4 800 54 L800 240 L0 240 Z" fill="var(--band)"/>
  </svg>

  <div class="info">
    <p class="dates">November 24th - 25th</p>
    <p class="times">Showtimes <b>3:00PM</b> &amp; <b>7:30PM</b> Saturday, <b>2:00PM</b> Sunday</p>
    <p class="tickets">Tickets available at <a href="#">www.DorvaSeats.example</a></p>
    <p class="contact">For more information contact <b>Dorva Theatre</b> @ <b>505.555.0147</b></p>
  </div>
</div>
</body>
</html>
```